Law firm business card

Information:

Me Marisa Delacourt

website: velmont-juris.ca
email: marisa@velmont-juris.ca
Phone: 514 372-5106
Fax: 514 372-5107

Address:
Delacourt and associates
2917 Brisebois
Montreal, QC
H3K 2T9

Areas of Expertise:
Franchise Agreements, Financing, Acquisition, Real Estate Development, Commercial Agreements and Corporate Law

Target Market(s)

executives, companie managers

Industry/Entity Type

Business

Colors
f78f20
000000

Requirements
Must have
• Must use the logo, the logo is available here:

https://www.filevault-share.net/sh/qe82kd0pl1m7/BXtr9LmQw3zPaYkN

```html
<!DOCTYPE html>
<html lang="en">
<head>
<meta charset="utf-8">
<title>Delacourt &amp; Associates — Business Card</title>
<link href="https://fonts.googleapis.com/css2?family=Exo+2:wght@400;500;600&display=swap" rel="stylesheet">
<style>
  :root {
    --orange: #f78f20;
    --orange-light: #fbb25f;
    --ink: #000000;
    --ink-soft: #3a3a3a;
    --paper: #ffffff;
    --backdrop: #e6e7e8;
  }
  * { margin: 0; padding: 0; box-sizing: border-box; }
  html, body { width: 1200px; height: 772px; overflow: hidden; }
  body {
    background: var(--backdrop);
    font-family: "Exo 2", sans-serif;
    position: relative;
  }
  .card {
    position: absolute;
    top: 231px;
    width: 540px;
    height: 309px;
    background: var(--paper);
    box-shadow: 0 6px 18px rgba(0,0,0,.18);
    overflow: hidden;
  }
  .card--front { left: 40px; }
  .card--back { left: 620px; }
  .card__shapes { position: absolute; inset: 0; }

  .brand {
    position: absolute;
    display: flex;
    align-items: center;
    gap: 14px;
  }
  .brand__dot {
    width: 46px; height: 46px;
    border: 2px solid var(--orange);
    border-radius: 50%;
    flex: none;
  }
  .brand__rule { width: 1px; height: 52px; background: var(--ink-soft); flex: none; }
  .brand__name {
    color: var(--orange);
    font-weight: 500;
    font-size: 26px;
    letter-spacing: 1px;
    line-height: 1.05;
    text-transform: uppercase;
  }
  .card--front .brand { left: 88px; top: 124px; }
  .card--back .brand { left: 30px; top: 118px; gap: 10px; }
  .card--back .brand__dot { width: 34px; height: 34px; }
  .card--back .brand__rule { height: 40px; }
  .card--back .brand__name { font-size: 18px; }

  .holder {
    position: absolute;
    left: 30px; top: 14px;
    color: var(--paper);
  }
  .holder__name { font-size: 17px; font-weight: 600; letter-spacing: 1.5px; text-transform: uppercase; }
  .holder__title { font-size: 11px; font-weight: 400; letter-spacing: .5px; margin-top: 2px; }

  .contacts {
    position: absolute;
    right: 26px; top: 104px;
    list-style: none;
    text-align: right;
  }
  .contacts li {
    display: flex;
    justify-content: flex-end;
    align-items: center;
    gap: 8px;
    font-size: 12.5px;
    color: var(--ink);
    height: 22px;
  }
  .icon { width: 15px; height: 15px; flex: none; }

  .address {
    position: absolute;
    right: 26px; bottom: 14px;
    display: flex; align-items: center; gap: 8px;
    color: var(--paper);
    font-size: 12.5px;
    line-height: 1.4;
    text-align: right;
  }
</style>
</head>
<body>

  <section class="card card--front" aria-label="Card front">
    <div class="brand">
      <span class="brand__dot"></span>
      <span class="brand__rule"></span>
      <span class="brand__name">Delacourt<br>&amp; Associates</span>
    </div>
  </section>

  <section class="card card--back" aria-label="Card back">
    <svg class="card__shapes" viewBox="0 0 540 309" preserveAspectRatio="none">
      <path d="M0 0H540V44C400 48 250 112 0 84Z" fill="var(--orange-light)"/>
      <path d="M0 0H540V36C400 40 250 102 0 74Z" fill="var(--orange)"/>
      <path d="M0 309H540V222C420 216 290 262 0 282Z" fill="var(--orange-light)"/>
      <path d="M0 309H540V230C420 224 290 270 0 290Z" fill="var(--orange)"/>
    </svg>

    <div class="holder">
      <p class="holder__name">Marisa Delacourt</p>
      <p class="holder__title">Managing Director</p>
    </div>

    <div class="brand">
      <span class="brand__dot"></span>
      <span class="brand__rule"></span>
      <span class="brand__name">Delacourt<br>&amp; Associates</span>
    </div>

    <ul class="contacts">
      <li>514 372-5106
        <svg class="icon" viewBox="0 0 16 16"><rect width="16" height="16" rx="3" fill="var(--orange)"/><path d="M5 3.5l2 2-1 1.2c.6 1.3 1.6 2.3 2.8 2.8l1.2-1 2 2-1.2 1.5C7.5 11.7 4.3 8.5 3.5 5z" fill="var(--paper)"/></svg>
      </li>
      <li>514 372-5107
        <svg class="icon" viewBox="0 0 16 16"><rect width="16" height="16" rx="3" fill="var(--orange)"/><rect x="4" y="6" width="8" height="6" rx="1" fill="var(--paper)"/><rect x="5.5" y="3" width="5" height="3" fill="var(--paper)"/></svg>
      </li>
      <li>marisa@velmont-juris.ca
        <svg class="icon" viewBox="0 0 16 16"><rect width="16" height="16" rx="3" fill="var(--orange)"/><rect x="3.5" y="5" width="9" height="6.5" fill="var(--paper)"/><path d="M3.5 5l4.5 3.5L12.5 5" fill="none" stroke="var(--orange)" stroke-width="1"/></svg>
      </li>
      <li>velmont-juris.ca
        <svg class="icon" viewBox="0 0 16 16"><rect width="16" height="16" rx="3" fill="var(--orange)"/><circle cx="8" cy="8" r="4.5" fill="none" stroke="var(--paper)" stroke-width="1.2"/><path d="M3.5 8h9M8 3.5c-2 2.5-2 6.5 0 9M8 3.5c2 2.5 2 6.5 0 9" fill="none" stroke="var(--paper)" stroke-width=".9"/></svg>
      </li>
    </ul>

    <div class="address">
      <p>2917 Brisebois, Montreal, QC<br>H3K 2T9</p>
      <svg class="icon" viewBox="0 0 16 16"><rect width="16" height="16" rx="3" fill="var(--paper)"/><path d="M8 13s-3.5-3.8-3.5-6.3a3.5 3.5 0 017 0C11.5 9.2 8 13 8 13z" fill="var(--orange)"/><circle cx="8" cy="6.7" r="1.3" fill="var(--paper)"/></svg>
    </div>
  </section>

</body>
</html>
```